Olmo Restaurant & Bar Menu

Want to make current menu more trendy in design. I have attached a pdf of the menu and of the logo. Rather, than being 6 pages I would like to make the menu into "4 pages". The menu will be printed in color.

I am open to designs that will allow the menu to be printed on 11x17 paper that will be folded in half. The "Breakfast" section needs to be its own page and all the way on the back.

As for the cover I am open to just keeping it as a cover with the info I have on it but completely different design/picture change. The logo needs to stay. The cover can also be used as having menu items on there if pulled of correctly.

The readability has to be clear to the guests.

The restaurant is a Mediterranean style and for the area it is priced mid-high. The atmosphere is casual fine dining with Martini & Wine Bar. All are ingredients are fresh never frozen and everything is prepared from scratch.

Industry/Entity Type

Restaurant

Requirements
Must have
• Breakfast on its own page on the back.
Nice to have
• Trendy Design

```html
<!DOCTYPE html>
<html lang="en">
<head>
<meta charset="utf-8">
<title>Olmo Restaurant &amp; Bar – Breakfast Menu</title>
<link href="https://fonts.googleapis.com/css2?family=Carlito:wght@400;700&display=swap" rel="stylesheet">
<style>
  :root {
    --ink: #050505;
    --ornament-a: #1b1b1b;
    --ornament-b: #0a0a0a;
    --accent: #1aa6e8;
    --accent-deep: #0f8fd0;
    --white: #ffffff;
    --tab-grey: #4a4a4a;
  }
  * { margin: 0; padding: 0; box-sizing: border-box; }
  html, body { width: 1200px; height: 777px; overflow: hidden; background: var(--ink); }
  body { font-family: "Carlito", "Calibri", sans-serif; color: var(--white); }

  .menu-spread { position: relative; width: 1200px; height: 777px; overflow: hidden; }
  .ornament-bg {
    position: absolute; inset: 0;
    background: radial-gradient(ellipse at 30% 40%, var(--ornament-a), var(--ornament-b) 70%);
  }

  /* side tabs */
  .side-tab { position: absolute; left: 0; width: 12px; background: var(--accent); }
  .side-notch { position: absolute; left: 0; width: 36px; height: 6px; background: var(--tab-grey); }

  .fold-line { position: absolute; left: 599px; top: 40px; width: 1px; height: 695px; background: var(--white); }

  /* breakfast page */
  .page-title { position: absolute; left: 0; width: 600px; top: 38px; text-align: center; }
  .page-title h1 { font-size: 17px; font-weight: 700; color: var(--accent); line-height: 20px; }
  .page-title p { font-size: 17px; line-height: 22px; }

  .menu-section { position: absolute; left: 71px; width: 480px; }
  .menu-section h2 { font-size: 11.5px; font-weight: 700; line-height: 14px; margin-bottom: 1px; }
  .item { font-size: 11px; font-weight: 700; color: var(--accent); line-height: 13px; }
  .item.plain { color: var(--white); }
  .item.indent { padding-left: 14px; }
  .desc { font-size: 8px; color: var(--accent); line-height: 12px; margin-bottom: 1px; }
  .desc.light { color: #d0d0d0; line-height: 10px; width: 200px; }

  /* cover */
  .cover-frame {
    position: absolute; left: 737px; top: 0; width: 321px; height: 658px;
    border: 8px solid var(--accent); border-top: 0; background: var(--ink);
  }
  .cover-photo {
    position: absolute; left: 0; top: 0; width: 305px; height: 345px;
    background: linear-gradient(180deg, #6fb6e6 0%, #b9d8ea 22%, #6b8a58 40%, #2b5f72 55%, #6a6a5e 70%, #f2f2f2 85%, #1a1a1a 100%);
  }
  .brand { position: absolute; left: 0; width: 305px; top: 380px; display: flex; align-items: center; justify-content: center; gap: 10px; }
  .brand-dot { width: 34px; height: 34px; border-radius: 50%; background: var(--accent); flex: none; }
  .brand-name { font-size: 27px; font-weight: 700; color: var(--white); line-height: 28px; text-transform: uppercase; }
  .cover-info { position: absolute; left: 0; width: 305px; text-align: center; font-weight: 700; font-size: 14px; line-height: 19px; }
  .cover-info.contact { top: 486px; }
  .cover-info.hours { top: 558px; color: var(--accent); }
  .cover-info.services { top: 594px; }

  .menu-tab {
    position: absolute; left: 824px; top: 658px; width: 146px; height: 119px;
    background: var(--accent); display: flex; align-items: flex-end; justify-content: center; padding-bottom: 28px;
  }
  .menu-tab span { font-size: 26px; color: var(--white); letter-spacing: 1px; }
</style>
</head>
<body>
<main class="menu-spread">
  <div class="ornament-bg" role="img" aria-label="Dark baroque scrollwork pattern in grey on black"></div>

  <div class="side-tab" style="top:40px;height:56px"></div>
  <div class="side-notch" style="top:96px"></div>
  <div class="side-tab" style="top:108px;height:124px"></div>
  <div class="side-notch" style="top:233px"></div>
  <div class="side-tab" style="top:245px;height:168px"></div>
  <div class="side-notch" style="top:420px"></div>
  <div class="side-tab" style="top:432px;height:112px"></div>
  <div class="side-notch" style="top:548px"></div>
  <div class="side-tab" style="top:560px;height:175px"></div>

  <div class="fold-line"></div>

  <header class="page-title">
    <h1>Breakfast</h1>
    <p>Served Saturday &amp; Sunday</p>
  </header>

  <section class="menu-section" style="top:99px">
    <h2>Skillets</h2>
    <div class="item">Veggie $6.95</div>
    <div class="desc">Skillet full of hash browns, onions, peppers, tomatoes &amp; mushrooms topped with cheese and 2 eggs. Served w/ Toast.</div>
    <div class="item">Irish $7.95</div>
    <div class="desc">Skillet full of hash browns, onions, peppers &amp; mushrooms topped with cheese and 2 eggs. Served w/ Toast.</div>
    <div class="item">Melting Pot $8.95</div>
    <div class="desc">Skillet full of hash browns, ham, bacon, sausage, mushrooms, onions, tomatoes and peppers topped with cheese and 2 eggs.<br>Served with toast.</div>
    <div class="item plain">Biscuits &amp; Gravy $7.95</div>
    <div class="desc" style="color:#e6e6e6">Skillet full of hash browns, onions, peppers &amp; cheese. Topped w/ homemade biscuit, sausage gravy &amp; 2 eggs.</div>
  </section>

  <section class="menu-section" style="top:239px">
    <h2>Omelettes</h2>
    <div class="desc">Fluffy Pan-Fried Omelettes, Served w/ Hash Browns &amp; Toast</div>
    <div class="item">Athenian $8.95</div>
    <div class="desc">Gyro off-the-cone, tomatoes, onions, olives, &amp; feta cheese. Served with side of homemade cucumber sauce.</div>
    <div class="item">Denver $7.95</div>
    <div class="desc">Ham, onion, pepper &amp; cheese.</div>
    <div class="item">Veggie $7.95</div>
    <div class="desc">Onions, peppers, tomatoes &amp; mushrooms.</div>
    <div class="item">Deluxe $8.95</div>
    <div class="desc">Ham, bacon, sausage, mushrooms, onions, tomatoes and peppers.</div>
    <div class="item">Spinach Pesto $8.95</div>
    <div class="desc">Sun-Dried tomatoes, spinach, mushrooms &amp; cheese. Topped w/ Pesto Cream Sauce</div>
    <div class="item">Ham &amp; Cheese $6.95</div>
  </section>

  <section class="menu-section" style="top:424px;width:260px">
    <h2>Pancakes, French Toast &amp; Waffles</h2>
    <div class="item">Apple Danish French Toast $6.95</div>
    <div class="item">Bananas Foster Pancakes $7.95</div>
    <div class="item">Strawberry Cake Waffle $7.95</div>
    <div class="item">Pancakes or French Toast (2) $4.55 / (3) $4.95</div>
    <div class="item">Belgium Waffle $4.95</div>
    <div class="item">Add Fruit Topping, Bacon, Ham or Sausage $1.95</div>
  </section>

  <section class="menu-section" style="top:424px;left:341px;width:240px">
    <h2>Light Breakfast</h2>
    <div class="item">Egg, Sausage, &amp; Cheese Sand. $4.25</div>
    <div class="item">Oatmeal or Cereal $3.55 w/ raisins $3.95</div>
    <div class="item">Bagel w/ cream cheese $2.55</div>
    <div class="item">English Muffin or Raisin Toast $1.55</div>
    <div class="item">Fresh Fruit Bowl $4.95</div>
    <div class="item plain">Mediterranean Pita $6.95</div>
    <div class="desc light">Pesto Spread on Pita Bread w/ spinach, tomatoes, feta &amp; an Egg.</div>
  </section>

  <section class="menu-section" style="top:554px">
    <h2>Eggs &amp; Specialties</h2>
    <div class="item">Two Eggs, Hash Browns &amp; Toast $4.95</div>
    <div class="item indent">With Bacon, Sausage or Ham $5.95</div>
    <div class="item indent">With Corned Beef Hash $6.55</div>
    <div class="item indent">With Gyro off-the-cone $6.95</div>
    <div class="item">Steak &amp; Eggs $13.95</div>
    <div class="desc">8oz Prime Cut Steak, 2 Eggs, hash browns, &amp; Toast.</div>
    <div class="item">Chop Steak &amp; Eggs $9.95</div>
    <div class="desc">10oz Chopped Sirloin Steak, 2 Eggs, hash browns, &amp; Toast.</div>
    <div class="item">Granny's Breakfast $6.95</div>
    <div class="desc">Two Eggs scrambled w/ potatoes, ham, onions &amp; peppers topped w/ cheese. Served with toast.</div>
    <div class="item">3 Deuces $6.95</div>
    <div class="desc">Two Eggs, Two Pancakes &amp; Two Sausage Links or Bacon Strips.</div>
    <div class="item">Homemade Biscuits &amp; Gravy Half $3.95 / Full $5.55</div>
  </section>

  <aside class="cover-frame">
    <div class="cover-photo" role="img" aria-label="Photo of a wine bottle, glasses of red and white wine, grapes and a plate of feta and olives on a table before a mountain lake"></div>
    <div class="brand">
      <span class="brand-dot"></span>
      <span class="brand-name">Olmo Restaurant<br>&amp; Bar</span>
    </div>
    <p class="cover-info contact">48 N Lakeview St · Maple Falls, WI 53999<br>262-555-0148<br>www.olmorestaurant.com</p>
    <p class="cover-info hours">Serving Breakfast Saturday &amp; Sunday</p>
    <p class="cover-info services">Catering &amp; Private Party Hosting Available<br>Friday Fish Fry · Saturday Prime Rib</p>
  </aside>

  <div class="menu-tab"><span>menu</span></div>
</main>
</body>
</html>
```